Product label for premium fruit wooden crates

Background: Kiralo offers premium quality fruits airflown (i.e. Japan, USA, Australia, etc) to Singapore at an affordable price. This includes exquisite and limited fruits like Shine Muscat grape, Shizuoka Ember Melon, Yellow Dragon Fruit, Fei zi xiao seedless lychee, Yellow Peaches, etc.

Requirements:

- Design a premium fruit’s label strap for identification and brand marketing.

- This strap will be used to tie around our fruit gift crate and fruit boxes (see attached).

- the logo use in this strap may use different color that must fit the 2 ribbons that will be used together with the crate box (see attached), red and gold ribbons(purl satin)

- the fruit crates and boxes will be presented as gift for vip, families, and working partners (important people)

This label will be printed in paper and tie around the fruit crate or paper box.

Web: www.kiralo.sg
FB: https://www.pagenest.net/krlorchard/
IG: https://www.snapgrid.net/krlorchard

Target Market(s)

Working class, families, expat, business clients (late 20 – 40s)

Industry/Entity Type

Gift Shop

Other font styles liked:
• Sakkal Majalla

Requirements
Must have
• - color that fit the 2 ribbons color (red and gold)
• - premium, luxury and exquisite feel
• - presentable as a gift to someone important
• - Kiralo's logo
• - The word 'KIRALO',
Nice to have
• the following words:
• - www.kiralo.sg; or/and
• - online premium fruits or/and
• - premium quality (No preference. let the designer choose)
• must be able to give customer a feel that Kiralo sells premium fruits
Should not have
• cant think of it now

```html
<!DOCTYPE html>
<html lang="en">
<head>
<meta charset="utf-8">
<title>Kiralo – Premium Fruits Label</title>
<link rel="stylesheet" href="https://fonts.googleapis.com/css2?family=Crimson+Pro:ital,wght@1,600&family=Cormorant+Garamond:wght@600&display=swap">
<style>
  :root {
    --canvas-bg: #ffffff;
    --label-red: #8c1a20;
    --gold-light: #fbec7a;
    --gold-mid: #efd04e;
    --gold-deep: #d4a23a;
    --brand-pink: #f27b84;
    --name-gold: #e6c81c;
  }
  html, body {
    margin: 0;
    padding: 0;
    width: 1200px;
    height: 750px;
    overflow: hidden;
    background: var(--canvas-bg);
  }
  .label {
    display: block;
    width: 1200px;
    height: 750px;
  }
  .label-outline {
    fill: url(#goldFoil);
    stroke: var(--label-red);
    stroke-width: 8;
    stroke-linejoin: round;
  }
  .brand-mark {
    font-family: "Crimson Pro", serif;
    font-style: italic;
    font-weight: 600;
    font-size: 52px;
    fill: var(--name-gold);
  }
  .headline {
    font-family: "Crimson Pro", serif;
    font-style: italic;
    font-weight: 600;
    font-size: 66px;
    fill: var(--label-red);
  }
  .brand-name {
    font-family: "Cormorant Garamond", serif;
    font-weight: 600;
    font-size: 40px;
    letter-spacing: 1px;
    fill: var(--brand-pink);
  }
  .web-address {
    font-family: "Cormorant Garamond", serif;
    font-weight: 600;
    font-size: 21px;
    letter-spacing: 1px;
    fill: var(--label-red);
  }
</style>
</head>
<body>
<svg class="label" viewBox="0 0 800 500" xmlns="http://www.w3.org/2000/svg" role="img" aria-label="Kiralo premium fruits label">
  <defs>
    <radialGradient id="goldFoil" cx="45%" cy="45%" r="65%">
      <stop offset="0%" stop-color="var(--gold-light)"/>
      <stop offset="55%" stop-color="var(--gold-mid)"/>
      <stop offset="100%" stop-color="var(--gold-deep)"/>
    </radialGradient>
  </defs>

  <path class="label-outline"
        d="M36 132 L232 132 C260 60 330 30 400 30 C470 30 540 60 568 132 L764 132
           L706 248 L764 364 L568 364 C540 440 470 470 400 470 C330 470 260 440 232 364
           L36 364 L94 248 Z"/>

  <text class="brand-mark" x="400" y="168" text-anchor="middle">Kiralo</text>

  <text class="headline" x="400" y="300" text-anchor="middle">Premium Fruits</text>

  <text class="brand-name" x="400" y="376" text-anchor="middle">KIRALO</text>

  <text class="web-address" x="400" y="414" text-anchor="middle">www.kiralo.sg</text>
</svg>
</body>
</html>
```